Engineering Consultant Business Card

I'm starting a new business as a high-end engineering consultant in a niche field. I've attached the jpg for my logo plus the branding guideline document that I've been following. You can see my business website here: www.tarvikworks.com
I'd like a business card that has the logo on one side, then the other side has (in any order): Tarvik Works, Inc.
Dana Whitlock
President and Chief EMC Engineer
www.tarvikworks.com
dana@tarvikworks.com
Optional: motto "We will solve your EMC problems as early as possible—ideally before they even start."
I'm not planning on including a phone number
Target Market(s)
Businesses, especially makers of electronics hardware
Industry/Entity Type
Electrical engineering
Contact Information for Business Card
Company name, my name, website, email

```html
<!DOCTYPE html>
<html lang="en">
<head>
<meta charset="utf-8">
<title>Tarvik Works, Inc. — Business Card</title>
<link href="https://fonts.googleapis.com/css2?family=Public+Sans:wght@400;600;700&display=swap" rel="stylesheet">
<style>
  :root {
    --page-bg: #5f5f62;
    --brand-blue: #27399a;
    --pattern-dark: #2a3b9e;
    --pattern-light: #3552c4;
    --card-white: #ffffff;
    --ink: #1f1f24;
    --rule: #2a2a2f;
  }
  * { margin: 0; padding: 0; box-sizing: border-box; }
  html, body {
    width: 900px; height: 1200px; overflow: hidden;
    background: var(--page-bg);
    font-family: "Public Sans", Arial, sans-serif;
  }
  .canvas { position: relative; width: 900px; height: 1200px; }

  .card {
    position: absolute; left: 135px; width: 632px;
    border-radius: 15px; overflow: hidden;
  }

  /* Front */
  .card-front { top: 215px; height: 357px; }
  .front-pattern {
    position: absolute; inset: 0;
    background: linear-gradient(110deg, var(--pattern-dark) 0%, var(--pattern-light) 100%);
  }
  .front-mark {
    position: absolute; left: 50%; top: 50%;
    transform: translate(-50%, -50%);
    display: flex; align-items: center; gap: 10px;
    color: var(--card-white);
    font-weight: 700; font-size: 20px; letter-spacing: 0.04em;
    white-space: nowrap;
  }
  .front-mark .dot {
    width: 14px; height: 14px; border-radius: 50%;
    background: var(--card-white);
  }

  /* Back */
  .card-back { top: 628px; height: 359px; background: var(--card-white); }
  .back-mark {
    position: absolute; left: 40px; top: 156px; width: 256px;
    display: flex; align-items: center; gap: 10px;
    color: var(--brand-blue);
    font-weight: 700; font-size: 27px; line-height: 1;
    white-space: nowrap;
  }
  .back-mark .dot {
    width: 22px; height: 22px; border-radius: 50%;
    background: var(--brand-blue); flex: none;
  }
  .divider {
    position: absolute; left: 315px; top: 128px;
    width: 1.5px; height: 105px; background: var(--rule);
  }
  .contact { position: absolute; left: 346px; top: 124px; }
  .contact-name {
    color: var(--brand-blue); font-weight: 700;
    font-size: 25px; line-height: 1; letter-spacing: 0.01em;
  }
  .contact-title {
    margin-top: 10px; color: var(--ink);
    font-size: 14.5px; font-weight: 400; letter-spacing: 0.02em;
  }
  .contact-list { list-style: none; margin-top: 16px; }
  .contact-list li {
    display: flex; align-items: center; gap: 9px;
    color: var(--ink); font-size: 14.5px; letter-spacing: 0.02em;
    height: 24px;
  }
  .contact-list svg { width: 16px; height: 16px; flex: none; }

  .motto-band {
    position: absolute; left: 0; right: 0; top: 302px; height: 35px;
    background: var(--brand-blue);
    display: flex; align-items: center; justify-content: center;
    color: var(--card-white); font-weight: 600; font-size: 14px;
    white-space: nowrap;
  }
</style>
</head>
<body>
<main class="canvas">

  <section class="card card-front" aria-label="Card front">
    <div class="front-pattern" role="img" aria-label="Repeating embossed brand-mark pattern in tonal blue"></div>
    <div class="front-mark"><span class="dot"></span>Tarvik Works</div>
  </section>

  <section class="card card-back" aria-label="Card back">
    <div class="back-mark"><span class="dot"></span>Tarvik Works</div>
    <div class="divider"></div>
    <div class="contact">
      <h1 class="contact-name">DANA WHITLOCK</h1>
      <p class="contact-title">President and Chief EMC Engineer</p>
      <ul class="contact-list">
        <li>
          <svg viewBox="0 0 16 16" aria-hidden="true">
            <rect x="1" y="3" width="14" height="10" fill="var(--brand-blue)"/>
            <path d="M1.5 3.5 L8 9 L14.5 3.5 M1.5 12.5 L6 8 M14.5 12.5 L10 8" stroke="#fff" stroke-width="1.2" fill="none"/>
          </svg>
          dana@tarvikworks.com
        </li>
        <li>
          <svg viewBox="0 0 16 16" aria-hidden="true" fill="none" stroke="var(--brand-blue)" stroke-width="1.3">
            <circle cx="8" cy="8" r="6.5"/>
            <ellipse cx="8" cy="8" rx="3" ry="6.5"/>
            <path d="M1.5 8 H14.5 M2.5 4.8 H13.5 M2.5 11.2 H13.5"/>
          </svg>
          www.tarvikworks.com
        </li>
      </ul>
    </div>
    <div class="motto-band">We will solve your EMC problems as early as possible—ideally before they even start.</div>
  </section>

</main>
</body>
</html>
```